redesign my website bluekelpvoyages.com and make it user friendly

I already have a website, bluekelpvoyages.com, and want a redesign in WordPress with Elementor Pro, using the same text/content. The goal is to improve:

Design quality (colors, fonts, spacing, visual flow)
User experience (easy navigation, clear offers)
Conversion readiness (calls-to-action, trust signals, booking flow)
Technical side (SEO basics, fast speed, full mobile responsiveness)

The site should look modern, clean, fun, engaging, interactive and optimized for speed and usability.

I would like the 11 page to be consolidate dto 6 as follows: Home (main landing, highlights)

Sailboat Trips (all packages, itineraries, pricing)
Boats (fleet details, features, photos)
How It Works (booking process, FAQs, travel info, what to expect)
Blog
Contact Us (form, WhatsApp, phone, etc.)

Target Market(s)

sailboat trip customers for Coral Mira Keys in Panama

Industry/Entity Type

Travel, Boat Tour Agency

Coding

Number of Pages Required

3 page

Font styles to use
Sans Serif
Other font styles liked:
• Oswalg and sans serif

Colors
0054AA
0677BA
7BADD7
CADEEF
E8F1F8
0094D4
00A9DD
6FCCEA
C7EBF8
E9F6FB
FFC000
F8CF3A
FAE287
FDF2CF
FEFAEE
F0912C
F2A743
F7CA91
FBE8D2
FDF5EE

Requirements
Must have
• Home (main landing, highlights) Sailboat Trips (all packages, itineraries, pricing) Boats (fleet details, features, photos) How It Works (booking process, FAQs, travel info, what to expect) Blog (updates, travel tips, inspiration) Contact Us (form, WhatsApp, phone, etc.)
Nice to have
• I want it to look professionla and be very user friendy to entice people to contact me to book boat trips
Should not have
• a store

```html
<!DOCTYPE html>
<html lang="en">
<head>
<meta charset="utf-8">
<title>Blue Kelp Voyages – Panama Sailing Vacations</title>
<link href="https://fonts.googleapis.com/css2?family=Oswald:wght@500;600&family=Lato:ital,wght@0,400;0,700;1,400&display=swap" rel="stylesheet">
<style>
:root{
  --orange:#ea953d;
  --blue:#0094d4;
  --blue-text:#3a9ad6;
  --nav:#4ba7dc;
  --ink:#222;
  --body:#555;
  --pale:#eef6fc;
  --footer:#cfe8f5;
  --line:#c9d3dc;
}
*{margin:0;padding:0;box-sizing:border-box}
html,body{width:1200px;height:3688px;overflow:hidden;background:#fff}
body{font-family:'Lato',sans-serif;color:var(--ink);position:relative}
.abs{position:absolute}
.heading{font-family:'Oswald',sans-serif;font-weight:600;text-transform:uppercase;color:var(--ink);letter-spacing:.3px}
.btn{position:absolute;display:flex;align-items:center;justify-content:center;background:var(--orange);color:#fff;font-weight:700;text-transform:uppercase;border-radius:30px;font-size:15px}
.btn.outline{background:#fff;color:var(--orange);border:2px solid var(--orange)}
.center{left:0;width:1200px;text-align:center}

/* header */
.brand{left:143px;top:14px;display:flex;align-items:center;gap:14px}
.brand-dot{width:40px;height:40px;border-radius:50%;background:var(--blue)}
.brand-name{font-family:'Oswald',sans-serif;font-weight:600;font-size:27px;color:var(--ink);text-transform:uppercase}
.follow{left:732px;top:10px;font-size:12px}
.socials{left:733px;top:33px;display:flex;gap:8px}
.socials span{width:29px;height:29px;border-radius:50%;border:1px solid #ddd;display:block}
.socials span.on{background:var(--orange);border-color:var(--orange)}
.quote-top{left:879px;top:16px;width:176px;height:44px}
.nav{left:0;top:73px;width:1200px;height:48px;background:var(--nav)}
.nav ul{list-style:none;display:flex;position:absolute;left:145px;top:0;height:48px}
.nav li{color:#fff;font-size:15px;line-height:48px;padding:0 24px}
.nav li.active{background:var(--orange);padding:0 16px}

/* hero */
.hero{left:0;top:121px;width:1200px;height:580px;background:linear-gradient(180deg,#9db3ad 0%,#6d958a 22%,#4c9ba3 40%,#3f95a1 70%,#3a8c98 100%)}
.pill{left:487px;top:240px;width:227px;height:29px;background:#fff;border-radius:15px;color:var(--blue-text);font-size:11.5px;display:flex;align-items:center;justify-content:center}
.hero-title{top:285px;font-size:48px;line-height:65px;color:#fff;text-shadow:0 2px 6px rgba(0,0,0,.25)}
.arrow{width:36px;height:36px;border-radius:50%;background:rgba(40,40,40,.55);display:flex;align-items:center;justify-content:center}
.dots{display:flex;gap:6px}
.dots i{width:9px;height:9px;border-radius:50%;border:1.5px solid #fff;display:block}
.dots i.on{background:#fff}

/* about */
.about-photo{left:145px;top:737px;width:426px;height:426px;border-radius:50%;background:radial-gradient(circle at 50% 40%,#c9a78a,#6b5a48 70%,#3d3a33)}
.eyebrow{color:var(--blue-text);font-size:19px}
.para{font-size:13.5px;line-height:23.5px;color:var(--body)}

/* services */
.service{width:290px;text-align:center}
.service h3{font-weight:400;font-size:19px;margin:14px 0 10px}
.service p{font-size:13px;line-height:23px;color:var(--body)}

/* fleet */
.fleet-card{left:165px;top:1840px;width:864px;height:232px;background:#fff;border-radius:116px}
.fleet-photo{left:180px;top:1856px;width:200px;height:200px;border-radius:50%;background:linear-gradient(160deg,#3fb0c8,#1d7fa5 60%,#145f84)}
.spec{width:70px;text-align:center;font-size:13px;color:#333}

/* testimonials */
.avatar{border-radius:50%;border:2px solid #fff;box-shadow:0 0 0 1px #ddd}
.quote{left:170px;top:2473px;width:860px;text-align:center;font-style:italic;font-size:12px;line-height:24px;color:#555}
.quote-mark{font-family:'Oswald',sans-serif;font-size:60px;color:#d9d9d9;line-height:1}
.vdots i{display:block;width:9px;height:9px;border-radius:50%;background:#e5e5e5;margin-bottom:7px}
.vdots i.on{background:var(--orange)}

/* contact */
.field{position:absolute;height:47px;border:1px solid var(--line);border-radius:4px;background:#fff}
.field label{position:absolute;left:18px;top:-10px;background:#fff;padding:0 6px;font-size:13px;color:#333}
.field .val{position:absolute;left:18px;top:16px;font-size:11px;color:#999}
.field .ico{position:absolute;right:14px;top:16px}
.question{left:143px;top:2960px;font-size:14px;color:#333}
.opt{font-size:12.5px;color:#555;display:flex;align-items:center;gap:7px}
.opt b{width:11px;height:11px;border-radius:50%;border:1.5px solid #777;display:block}
.opt.checked{color:var(--blue-text)}
.opt.checked b{border-color:var(--blue);background:var(--blue)}

/* footer */
.foot-links{top:3452px;left:153px;width:892px;display:flex;justify-content:space-between;font-size:15px;color:#222}
.rule{left:143px;width:912px;height:1px;background:#b9d3e3}
.contact-ico{width:48px;height:48px;border-radius:50%;background:var(--orange);display:flex;align-items:center;justify-content:center}
.c-label{font-family:'Oswald',sans-serif;font-size:15px;color:var(--blue-text);text-transform:uppercase}
.c-value{font-size:15px;color:#222;margin-top:3px;white-space:nowrap}
.c-note{font-size:11px;color:#333;margin-top:4px}
</style>
</head>
<body>

<!-- Header -->
<div class="abs brand"><span class="brand-dot"></span><span class="brand-name">Blue Kelp Voyages</span></div>
<div class="abs follow">Follow Us</div>
<div class="abs socials"><span></span><span class="on"></span><span></span></div>
<div class="btn quote-top">Request a Quote</div>
<nav class="abs nav">
  <ul>
    <li class="active">Home</li><li>Sailboat Trips</li><li>Boats</li><li>How It Works</li><li>Blog</li><li>Contact Us</li>
  </ul>
</nav>

<!-- Hero -->
<section class="abs hero" role="img" aria-label="Photo of a traveller diving from a catamaran into turquoise water beside a palm-lined island"></section>
<div class="abs pill">WELCOME TO CORAL MIRA KEYS</div>
<h1 class="abs center heading hero-title">Panama Sailingvacations.Ultimate<br>Beaches &amp; Catamaran Tours</h1>
<div class="btn" style="left:468px;top:435px;width:265px;height:46px">Charter Inquiry Form</div>
<div class="abs arrow" style="left:80px;top:324px"><svg width="12" height="12" viewBox="0 0 12 12"><path d="M8 1L3 6l5 5" fill="none" stroke="#fff" stroke-width="2"/></svg></div>
<div class="abs arrow" style="left:1084px;top:324px"><svg width="12" height="12" viewBox="0 0 12 12"><path d="M4 1l5 5-5 5" fill="none" stroke="#fff" stroke-width="2"/></svg></div>
<div class="abs dots" style="left:580px;top:582px"><i></i><i class="on"></i><i></i></div>
<svg class="abs" style="left:0;top:560px" width="1200" height="160" viewBox="0 0 1200 160">
  <path d="M0 20 C200 120 380 110 600 70 C820 30 1000 10 1200 70 L1200 160 L0 160Z" fill="#fff"/>
  <path d="M0 20 C140 90 300 110 470 100 C700 80 900 20 1200 40" fill="none" stroke="#2f8fd0" stroke-width="9"/>
  <path d="M350 130 C600 110 850 50 1200 55" fill="none" stroke="#cde6f6" stroke-width="10"/>
  <path d="M600 125 C800 100 1000 60 1200 62" fill="none" stroke="#e3f1fa" stroke-width="6"/>
</svg>

<!-- About -->
<div class="abs about-photo" role="img" aria-label="Group photo of smiling guests gathered around a table of food on a beach"></div>
<div class="abs eyebrow" style="left:633px;top:803px">Who We Are</div>
<h2 class="abs heading" style="left:633px;top:838px;font-size:34px">About Blue Kelp Voyages</h2>
<p class="abs para" style="left:633px;top:898px;width:428px">We're sailors and travelers with a love for exploration. When we first arrived in Coral Mira, its unique beauty and culture left a lasting impression. What began as a stop along our journey soon became something more we felt a strong connection to this place and a sincere respect for its people, traditions, and way of life.</p>
<div class="btn" style="left:633px;top:1047px;width:144px;height:44px">Read More</div>

<!-- Services -->
<svg class="abs" style="left:0;top:1165px" width="1200" height="560" viewBox="0 0 1200 560">
  <path d="M0 10 C200 60 380 80 600 50 C820 20 1000 0 1200 30 L1200 560 L0 560Z" fill="#eef6fc"/>
</svg>
<h2 class="abs center heading" style="top:1308px;font-size:34px">Discover Ultimate Panama Sailing Tours</h2>
<div class="abs service" style="left:125px;top:1375px">
  <svg width="80" height="80" viewBox="0 0 80 80" fill="none" stroke="#3a9ad6" stroke-width="3"><circle cx="40" cy="40" r="26"/><circle cx="40" cy="40" r="9"/><path d="M40 4v72M4 40h72M15 15l50 50M65 15L15 65"/></svg>
  <h3>Private Charters</h3>
  <p>Sail the beautiful islands and beaches of Coral Mira on a private all-inclusive catamaran.</p>
</div>
<div class="abs service" style="left:450px;top:1375px">
  <svg width="80" height="80" viewBox="0 0 80 80" fill="none" stroke="#3a9ad6" stroke-width="3"><path d="M40 70 L12 42 C2 32 8 14 22 14 C30 14 36 20 40 26 C44 20 50 14 58 14 C72 14 78 32 68 42Z" fill="#bfe2f5"/><path d="M26 46 l10 10 M34 40 l12 12 M42 34 l10 10"/></svg>
  <h3>Shared Charters</h3>
  <p>Share the experience with others for a more affordable alternative to a private charter.</p>
</div>
<div class="abs service" style="left:777px;top:1375px">
  <svg width="90" height="80" viewBox="0 0 90 80" fill="none" stroke="#3a9ad6" stroke-width="3"><path d="M8 52 L82 52 L72 64 L16 64Z"/><rect x="20" y="36" width="50" height="16"/><rect x="30" y="24" width="26" height="12"/><path d="M26 44h4M38 44h4M50 44h4M4 72 C20 66 30 78 45 72 C60 66 70 78 86 72"/></svg>
  <h3>Family Friendly Boat Trips</h3>
  <p>Coral Mira is perfect for kids, with calm waters, safe snorkeling, and fun island-hopping.</p>
</div>
<div class="btn" style="left:500px;top:1580px;width:200px;height:44px">Request a Quote</div>

<!-- Fleet -->
<svg class="abs" style="left:0;top:1670px" width="1200" height="545" viewBox="0 0 1200 545">
  <path d="M0 60 C150 30 300 10 500 40 C700 70 850 10 1000 20 C1100 25 1160 40 1200 50 L1200 480 C1050 540 850 540 650 500 C450 460 250 500 0 470Z" fill="#3b8fcc"/>
</svg>
<h2 class="abs center heading" style="top:1757px;font-size:32px;color:#fff">Featured Catamarans</h2>
<div class="abs fleet-card"></div>
<div class="abs fleet-photo" role="img" aria-label="Aerial photo of a white catamaran anchored in clear blue water"></div>
<div class="abs spec" style="left:393px;top:1856px">
  <svg width="36" height="26" viewBox="0 0 36 26" fill="none" stroke="#3a9ad6" stroke-width="2"><ellipse cx="14" cy="10" rx="12" ry="8"/><path d="M14 18h20v6H4v-6"/><path d="M10 18v3M16 18v3M22 18v3M28 18v3"/></svg>
  <div>42 ft</div>
</div>
<div class="abs spec" style="left:393px;top:1925px">
  <svg width="30" height="32" viewBox="0 0 30 32" fill="none" stroke="#3a9ad6" stroke-width="2"><path d="M15 2v8M8 10h14l4 10-11 8-11-8z"/><path d="M2 30c5-3 8 3 13 0s8 3 13 0"/></svg>
  <div>3 Cabin</div>
</div>
<div class="abs spec" style="left:393px;top:1997px">
  <svg width="36" height="28" viewBox="0 0 36 28" fill="none" stroke="#3a9ad6" stroke-width="2"><circle cx="18" cy="7" r="5"/><circle cx="7" cy="10" r="4"/><circle cx="29" cy="10" r="4"/><path d="M8 26c0-7 4-11 10-11s10 4 10 11M1 26c0-5 2-8 6-8M35 26c0-5-2-8-6-8"/></svg>
  <div>8 Guest</div>
</div>
<div class="abs" style="left:470px;top:1860px;width:1px;height:192px;background:#e3e3e3"></div>
<div class="abs" style="left:500px;top:1866px;font-size:16px;color:var(--blue-text)">CATAMARAN <span class="heading" style="font-size:16px;margin-left:12px">Marlin 42</span></div>
<div class="abs" style="left:500px;top:1899px;font-size:17px">Service That Exceeds All Expectations!</div>
<p class="abs para" style="left:500px;top:1928px;width:480px;font-size:13px">We started as strangers and left as friends! The crew made sure everyone felt welcome, and every moment was filled with fun and laughter.</p>
<div class="btn" style="left:500px;top:2000px;width:167px;height:44px">Info and Price</div>
<div class="btn outline" style="left:679px;top:2000px;width:215px;height:44px">See All Boats &amp; Prices</div>
<svg class="abs" style="left:128px;top:1944px" width="16" height="24" viewBox="0 0 16 24"><path d="M12 2L3 12l9 10" fill="none" stroke="#fff" stroke-width="3"/></svg>
<svg class="abs" style="left:1054px;top:1944px" width="16" height="24" viewBox="0 0 16 24"><path d="M4 2l9 10-9 10" fill="none" stroke="#fff" stroke-width="3"/></svg>
<div class="abs dots" style="left:580px;top:2102px"><i></i><i class="on"></i><i></i></div>

<!-- Testimonials -->
<h2 class="abs center heading" style="top:2258px;font-size:38px">What Our Clients Say</h2>
<svg class="abs" style="left:524px;top:2328px" width="152" height="26" viewBox="0 0 152 26">
  <g fill="#f5a623">
    <path id="st" d="M13 1l3.6 7.6 8.2 1-6 5.7 1.6 8.2L13 19.5 5.6 23.5l1.6-8.2-6-5.7 8.2-1z"/>
    <use href="#st" x="31"/><use href="#st" x="62"/><use href="#st" x="93"/><use href="#st" x="124"/>
  </g>
</svg>
<div class="abs avatar" style="left:423px;top:2380px;width:57px;height:57px;background:#e8cfb4" role="img" aria-label="Guest portrait"></div>
<div class="abs avatar" style="left:491px;top:2380px;width:57px;height:57px;background:#7fa6c2" role="img" aria-label="Guest portrait"></div>
<div class="abs avatar" style="left:558px;top:2369px;width:82px;height:82px;background:#5f7d57;box-shadow:0 0 0 2px #3a9ad6" role="img" aria-label="Featured guest portrait"></div>
<div class="abs avatar" style="left:650px;top:2380px;width:57px;height:57px;background:#5a6f8e" role="img" aria-label="Guest portrait"></div>
<div class="abs avatar" style="left:718px;top:2380px;width:57px;height:57px;background:#a46a50" role="img" aria-label="Guest portrait"></div>
<div class="abs quote-mark" style="left:150px;top:2438px">&ldquo;</div>
<p class="abs quote">My family and I sailed with Captain Rafo and Lise on the Brisa Azul for 4 days. It was the best possible experience. Rafo took care of our EVERY needs as a family. Moreover, because we were traveling with my elderly parents as well as younger kids, we needed a wide range of travel accommodations. Daniela from Blue Kelp Voyages did EVERYTHING. She was very responsive, and professional and took care of all of our requests, down to every last detail. I would absolutely book with her again and would recommend all my friends to do so as well. 10/10 experience!</p>
<div class="abs quote-mark" style="left:884px;top:2560px">&rdquo;</div>
<div class="abs center" style="top:2583px;font-size:16px;color:var(--blue-text)">- Marina Keller R</div>
<div class="abs vdots" style="left:1080px;top:2436px"><i></i><i></i><i class="on"></i><i></i><i></i></div>

<!-- Contact -->
<svg class="abs" style="left:0;top:2625px" width="1200" height="720" viewBox="0 0 1200 720">
  <path d="M0 30 C200 60 400 70 600 40 C800 10 1000 0 1200 30 L1200 720 L0 720Z" fill="#eef6fc"/>
</svg>
<h2 class="abs center heading" style="top:2725px;font-size:38px">Contact Us</h2>

<div class="field" style="left:143px;top:2810px;width:297px"><label>Full Name</label><span class="val">Jhone Duo</span>
  <svg class="ico" width="12" height="12" viewBox="0 0 12 12" fill="#999"><circle cx="6" cy="3.5" r="3"/><path d="M1 12c0-4 2-5.5 5-5.5s5 1.5 5 5.5z"/></svg></div>
<div class="field" style="left:451px;top:2810px;width:297px"><label>Whatsapp Number</label><span class="val">+1-888-888-8888</span>
  <svg class="ico" width="12" height="12" viewBox="0 0 12 12" fill="#999"><path d="M2 1l2.5-.5 1.5 3-1.5 1c.6 1.4 1.6 2.4 3 3l1-1.5 3 1.5-.5 2.5C6 11 1 6 2 1z"/></svg></div>
<div class="field" style="left:758px;top:2810px;width:297px"><label>Email Address</label><span class="val">guest@mailbox.com</span>
  <svg class="ico" width="12" height="10" viewBox="0 0 12 10" fill="#999"><rect width="12" height="10" rx="1"/><path d="M1 1l5 4 5-4" stroke="#fff" fill="none"/></svg></div>

<div class="field" style="left:143px;top:2888px;width:297px"><label>Number of Passengers</label><span class="val">1</span>
  <svg class="ico" width="8" height="14" viewBox="0 0 8 14" fill="#888"><path d="M4 0l4 5H0zM4 14l4-5H0z"/></svg></div>
<div class="field" style="left:451px;top:2888px;width:297px"><label>Number of Days</label><span class="val">4</span>
  <svg class="ico" width="8" height="14" viewBox="0 0 8 14" fill="#888"><path d="M4 0l4 5H0zM4 14l4-5H0z"/></svg></div>
<div class="field" style="left:758px;top:2888px;width:297px"><label>Date</label><span class="val">24/09/2025</span>
  <svg class="ico" width="12" height="12" viewBox="0 0 12 12" fill="none" stroke="#999"><rect x=".5" y="1.5" width="11" height="10"/><path d="M.5 4.5h11M3 0v3M9 0v3"/></svg></div>

<div class="abs question">What Type of Experience Are You Looking For? (Check All That Apply)</div>
<div class="abs opt" style="left:143px;top:2998px"><b></b>Relaxing and disconnected</div>
<div class="abs opt" style="left:143px;top:3022px"><b></b>Island-hopping adventure</div>
<div class="abs opt checked" style="left:340px;top:2998px"><b></b>Snorkeling &amp; marine life</div>
<div class="abs opt" style="left:340px;top:3022px"><b></b>Cultural exchange with the Guna people</div>
<div class="abs opt" style="left:611px;top:2998px"><b></b>Family-friendly</div>
<div class="abs opt" style="left:611px;top:3022px"><b></b>Romantic getaway</div>
<div class="abs opt" style="left:763px;top:2998px"><b></b>Food &amp; drink-focused</div>
<div class="abs opt" style="left:763px;top:3022px"><b></b>Sailing-focused</div>
<div class="abs opt" style="left:933px;top:2998px"><b></b>Budget-friendly</div>
<div class="abs opt" style="left:933px;top:3022px"><b></b>Luxury experience</div>

<div class="field" style="left:143px;top:3073px;width:912px;height:100px"><label>Message</label><span class="val" style="top:22px">Lorem ipsum dolor sit amet, consectetur adipiscing elit, sed do eiusmod tempoea ...</span>
  <svg class="ico" style="top:22px" width="12" height="10" viewBox="0 0 12 10" fill="#999"><ellipse cx="6" cy="4.5" rx="6" ry="4.5"/></svg></div>
<div class="btn" style="left:524px;top:3200px;width:152px;height:48px">Submit Now</div>

<!-- Footer -->
<svg class="abs" style="left:0;top:3300px" width="1200" height="388" viewBox="0 0 1200 388">
  <path d="M0 95 C180 20 350 20 560 45 C760 70 950 40 1200 70 L1200 388 L0 388Z" fill="#cfe8f5"/>
  <path d="M0 100 C150 30 320 15 520 35 C700 55 880 60 1200 30" fill="none" stroke="#2f8fd0" stroke-width="9"/>
  <path d="M380 70 C600 20 850 25 1200 45" fill="none" stroke="#8ac6ea" stroke-width="5"/>
</svg>
<div class="abs foot-links"><span>Home</span><span>|</span><span>Sailboat Trips</span><span>|</span><span>Boats</span><span>|</span><span>How It Works</span><span>|</span><span>Blog</span><span>|</span><span>Contact Us</span></div>
<div class="abs rule" style="top:3494px"></div>
<p class="abs" style="left:143px;top:3512px;width:380px;font-size:13.5px;line-height:27px;color:#222">Discover Unforgettable Catamaran and Sailboat Adventures In Guna Yala (Coral Mira), Panama. Blue Kelp Voyages LLC Offers All Inclusive Island Hopping, Snorkeling, and Immersive Cultural Experiences trusted By Travelers Worldwide.</p>
<div class="abs contact-ico" style="left:550px;top:3550px"><svg width="22" height="16" viewBox="0 0 22 16"><rect width="22" height="16" rx="2" fill="#fff"/><path d="M1 1l10 8 10-8" fill="none" stroke="#ea953d" stroke-width="2"/></svg></div>
<div class="abs" style="left:617px;top:3540px"><div class="c-label">Email Address</div><div class="c-value">sail@bluekelpvoyages.com</div><div class="c-note">Email Us on</div></div>
<div class="abs contact-ico" style="left:818px;top:3550px"><svg width="22" height="22" viewBox="0 0 22 22" fill="#fff"><path d="M5 3l4-1 2 5-2.5 1.5c1 2.2 2.8 4 5 5L15 11l5 2-1 4C11 18 4 11 5 3z"/></svg></div>
<div class="abs" style="left:882px;top:3540px"><div class="c-label">Whatsapp Number</div><div class="c-value">+57 300 555 0142</div><div class="c-note">Call Us Now</div></div>
<div class="abs rule" style="top:3640px"></div>
<div class="abs center" style="top:3658px;font-size:13px;color:#222">2025 Copyright © Blue Kelp Voyages - Privacy Policy - Terms &amp; Conditions</div>

</body>
</html>
```